Company PowerPoint Template to attract new customers

Looking for a set of template PowerPoint slides to use for my business. We sell a service where we sell products for brands. We need an Intro slide, slides that we can add text and images to and slides to show pricing. The slides do not need any 'content' as we have that - we just need something that looks attractive, and appealing. We want to draw people in and get them talking to us.

Target Market(s)

FMCG Businesses

Industry/Entity Type

FMCG Sales

Font styles to use
Sans Serif

Requirements
Must have
• A few variation of slide types

```html
<!DOCTYPE html>
<html lang="en">
<head>
<meta charset="utf-8">
<title>Bright Satchel – Presentation Template</title>
<link href="https://fonts.googleapis.com/css2?family=Montserrat:wght@500;600;700;800&family=Poppins:wght@400;500&display=swap" rel="stylesheet">
<style>
  :root{
    --canvas:#A6A7A9;
    --white:#FFFFFF;
    --ink:#151515;
    --body:#3A3A3A;
    --orange:#F39019;
    --panel-orange:#F7A53C;
    --pink:#E4234E;
    --magenta:#E0338A;
    --card:#F2F1F3;
    --rule:#C9C9C9;
    --chart-green:#8DC63F;
    --chart-pink:#E0157D;
    --grid:#E3E3E3;
  }
  *{box-sizing:border-box;margin:0;padding:0}
  html,body{width:1014px;height:1200px;overflow:hidden}
  body{background:var(--canvas);position:relative;font-family:'Poppins',sans-serif;color:var(--ink)}
  .slide{position:absolute;width:433px;height:243px;background:var(--white);overflow:hidden}
  .abs{position:absolute}

  .brand{position:absolute;left:16px;top:12px;display:flex;align-items:center;gap:4px}
  .brand-mark{width:14px;height:14px;background:var(--orange);border-radius:2px}
  .brand-name{font-family:'Montserrat',sans-serif;font-weight:800;color:var(--orange);font-size:7.5px;line-height:8px;letter-spacing:.2px}
  .brand--large .brand-mark{width:22px;height:22px}
  .brand--large .brand-name{font-size:11px;line-height:12px}

  .slide-title{position:absolute;left:100px;font-family:'Montserrat',sans-serif;font-weight:600;font-size:11px;line-height:22px;padding:0 4px;border-top:1px solid var(--ink);border-bottom:1px solid var(--ink)}

  /* Intro */
  .intro .bar-top{left:0;top:0;width:100%;height:3px;background:var(--orange)}
  .intro .bar-bottom{left:0;bottom:0;width:100%;height:3px;background:var(--pink)}
  .intro .brand{left:21px;top:30px}
  .intro-title{left:21px;top:91px;font-family:'Montserrat',sans-serif;font-weight:800;font-size:21px;line-height:24px}
  .intro-title span{color:var(--pink);display:block}
  .intro-lead{left:22px;top:144px;width:112px;font-size:7.3px;line-height:12.3px;color:var(--body)}
  .intro-visual{left:165px;top:30px;width:255px;height:178px;border-radius:60px 60px 90px 8px;background:linear-gradient(90deg,#C07A1E 0%,#B26A1E 45%,#9E2346 60%,#8E1B3C 100%)}

  /* Agenda */
  .agenda .bar-bottom{left:0;bottom:0;width:100%;height:3px;background:var(--orange)}
  .agenda-title{left:102px;top:15px;font-family:'Montserrat',sans-serif;font-weight:700;font-size:14px}
  .agenda-item{position:absolute;width:186px;height:24px}
  .agenda-item h4{font-family:'Montserrat',sans-serif;font-weight:600;font-size:8.3px;line-height:10px}
  .agenda-item p{font-size:6.4px;line-height:10px;color:var(--body)}
  .agenda-item .num{position:absolute;right:0;top:2px;font-family:'Montserrat',sans-serif;font-weight:700;font-size:7.8px;color:var(--pink)}
  .agenda-item .line{position:absolute;left:92px;right:0;top:13px;height:0;border-top:.7px solid var(--orange)}

  /* About */
  .about-title{left:16px;top:45px;font-family:'Montserrat',sans-serif;font-weight:600;font-size:12.5px;line-height:16.5px}
  .about-copy{left:16px;top:85px;width:163px;font-size:4.55px;line-height:6.8px;color:var(--body);text-align:justify}
  .about-copy p+p{margin-top:5.5px}
  .about-accent{left:204px;top:17px;width:4px;height:207px;background:var(--panel-orange)}
  .about-photo{left:208px;top:11px;width:216px;height:216px;background:linear-gradient(135deg,#6B7A70 0%,#3B3A3E 55%,#1E1E22 100%)}
  .about-underline{left:217px;top:227px;width:198px;height:4px;background:var(--pink)}

  /* Solutions */
  .solution{position:absolute;top:50px;width:124px;height:177px;border-radius:6px;overflow:hidden;background:var(--panel-orange)}
  .solution .photo{height:105px}
  .solution h3{font-family:'Montserrat',sans-serif;font-weight:600;font-size:7.3px;line-height:10px;color:var(--ink);padding:8px 10px 0}
  .solution p{font-size:5.3px;line-height:8px;color:#2B2B2B;padding:5px 10px 0}

  /* What we do */
  .service{position:absolute;background:var(--card);border-radius:6px;height:89px;padding:10px 10px 0}
  .service .icon{width:19px;height:19px;border-radius:3px;background:var(--magenta);display:block}
  .service h3{font-family:'Montserrat',sans-serif;font-weight:600;font-size:6.3px;line-height:8px;margin-top:10px}
  .service p{font-size:5.1px;line-height:6.9px;color:var(--body);margin-top:3px}

  /* We do it all */
  .all-photo{left:0;top:46px;width:215px;height:197px;border-top:3px solid var(--orange);border-right:3px solid var(--orange);border-top-right-radius:76px;background:linear-gradient(140deg,#7A6A66 0%,#C7BFB9 45%,#5A4A48 100%)}
  .all-block{position:absolute;left:233px;width:180px}
  .all-block h3{font-family:'Montserrat',sans-serif;font-weight:600;font-size:8.3px;line-height:10px}
  .all-block p{font-size:5.2px;line-height:8px;color:var(--body);margin-top:4px}
  .all-rule{left:229px;width:204px;height:0;border-top:.7px solid var(--magenta)}

  /* Invest */
  .chart{position:absolute;left:0;top:0}
  .chart text{font-family:'Poppins',sans-serif;font-size:3.8px;fill:#444}

  /* Thank you */
  .thanks{background:linear-gradient(115deg,#F4F4F4 0%,#E7E7E7 35%,#F2F2F2 60%,#E4E4E4 100%)}
  .thanks .brand-block{left:33px;top:78px;display:flex;align-items:center;gap:8px}
  .thanks .brand-block .brand-mark{width:40px;height:40px;background:var(--pink);border-radius:4px}
  .thanks .brand-block .brand-name{font-size:17px;line-height:20px;color:var(--orange)}
  .thanks-rule{left:214px;width:183px;height:0;border-top:.8px solid var(--orange)}
  .thanks-rule.pink{border-color:var(--pink)}
  .thanks-title{left:221px;top:99px;font-family:'Montserrat',sans-serif;font-weight:800;font-size:34px;color:var(--orange);letter-spacing:.3px}
</style>
</head>
<body>

<!-- Intro -->
<section class="slide intro" style="left:55px;top:55px">
  <div class="abs bar-top"></div>
  <div class="brand brand--large"><span class="brand-mark"></span><span class="brand-name">BRIGHT<br>SATCHEL</span></div>
  <h1 class="abs intro-title">BRIEF TO <span>BRILLIANT</span></h1>
  <p class="abs intro-lead">Lorem Ipsum is simply dummy text of the printing and types etting industry</p>
  <div class="abs intro-visual" role="img" aria-label="Photo of a briefcase in warm orange and crimson tones"></div>
  <div class="abs bar-bottom"></div>
</section>

<!-- Agenda -->
<section class="slide agenda" style="left:528px;top:55px">
  <div class="brand"><span class="brand-mark"></span><span class="brand-name">BRIGHT<br>SATCHEL</span></div>
  <h2 class="abs agenda-title">AGENDA</h2>
  <div class="agenda-item" style="left:17px;top:52px"><h4>Heading 1</h4><p>Lorem ipsum dolor sit am</p><span class="num">01</span><span class="line"></span></div>
  <div class="agenda-item" style="left:17px;top:82px"><h4>Heading 2</h4><p>Lorem ipsum dolor sit am</p><span class="num">02</span><span class="line"></span></div>
  <div class="agenda-item" style="left:17px;top:113px"><h4>Heading 3</h4><p>Lorem ipsum dolor sit am</p><span class="num">03</span><span class="line"></span></div>
  <div class="agenda-item" style="left:17px;top:144px"><h4>Heading 4</h4><p>Lorem ipsum dolor sit am</p><span class="num">04</span><span class="line"></span></div>
  <div class="agenda-item" style="left:17px;top:174px"><h4>Heading 5</h4><p>Lorem ipsum dolor sit am</p><span class="num">05</span><span class="line"></span></div>
  <div class="agenda-item" style="left:17px;top:205px"><h4>Heading 6</h4><p>Lorem ipsum dolor sit am</p><span class="num">06</span><span class="line"></span></div>
  <div class="agenda-item" style="left:237px;top:52px"><h4>Heading 7</h4><p>Lorem ipsum dolor sit am</p><span class="num">07</span><span class="line"></span></div>
  <div class="agenda-item" style="left:237px;top:82px"><h4>Heading 8</h4><p>Lorem ipsum dolor sit am</p><span class="num">08</span><span class="line"></span></div>
  <div class="agenda-item" style="left:237px;top:113px"><h4>Heading 9</h4><p>Lorem ipsum dolor sit am</p><span class="num">09</span><span class="line"></span></div>
  <div class="agenda-item" style="left:237px;top:144px"><h4>Heading 10</h4><p>Lorem ipsum dolor sit am</p><span class="num">10</span><span class="line"></span></div>
  <div class="agenda-item" style="left:237px;top:174px"><h4>Heading 11</h4><p>Lorem ipsum dolor sit am</p><span class="num">11</span><span class="line"></span></div>
  <div class="agenda-item" style="left:237px;top:205px"><h4>Heading 12</h4><p>Lorem ipsum dolor sit am</p><span class="num">12</span><span class="line"></span></div>
  <div class="abs bar-bottom"></div>
</section>

<!-- About -->
<section class="slide about" style="left:58px;top:333px">
  <div class="brand"><span class="brand-mark"></span><span class="brand-name">BRIGHT<br>SATCHEL</span></div>
  <h2 class="abs about-title">The Magic Behind<br>Bright Satchel</h2>
  <div class="abs about-copy">
    <p>At Bright Satchel, our goal isn't to be the biggest — it's to be the best. We connect brands and consumers through real experiences that advertising alone can't deliver. In a world full of noise, people trust what they can feel and try, and sampling puts that truth directly into their hands.</p>
    <p>We believe in authentic, human interaction, thoughtful targeting, and meaningful moments that create real impact. Quality beats quantity, and every activation is designed with creativity, care, and purpose. We use data responsibly, operate with transparency, and prioritise sustainability in everything we do.</p>
    <p>People are at the heart of our work. Our Brand Ambassadors are carefully selected and matched to each campaign to ensure genuine, memorable connections. And with every project, we learn, refine, and improve.</p>
    <p>Bright Satchel was born from a passion for bringing products to life. Today, we're experts in logistics, people, and delivering sampling experiences that lead to real adoption, loyalty, and growth — getting great products into the right hands, the right way.</p>
  </div>
  <div class="abs about-accent"></div>
  <div class="abs about-photo" role="img" aria-label="Team photo of brand ambassadors outdoors in a city"></div>
  <div class="abs about-underline"></div>
</section>

<!-- Solutions -->
<section class="slide solutions" style="left:528px;top:331px">
  <div class="brand"><span class="brand-mark"></span><span class="brand-name">BRIGHT<br>SATCHEL</span></div>
  <h2 class="slide-title" style="top:13px">Solutions</h2>
  <article class="solution" style="left:17px">
    <div class="photo" role="img" aria-label="Brand team engaging shoppers outside a store" style="background:linear-gradient(160deg,#8C8F95,#3A3C44)"></div>
    <h3>Experiential Marketing</h3>
    <p>Creating immersive, sensory brand moments that spark emotional connection, build trust, and drive meaningful action.</p>
  </article>
  <article class="solution" style="left:153px">
    <div class="photo" role="img" aria-label="Two staff members in a wholesale warehouse" style="background:linear-gradient(160deg,#9C7A55,#5A5550)"></div>
    <h3 style="padding-top:5px">Wholesale Cash &amp; Carry Depot Days</h3>
    <p>Engaging trade customers right at the point of influence strengthening relationships, shaping recommendations, and boosting in-store visibility.</p>
  </article>
  <article class="solution" style="left:291px">
    <div class="photo" role="img" aria-label="Hands passing a product sample box" style="background:linear-gradient(160deg,#B7BCC4,#4F5866)"></div>
    <h3>Sampling</h3>
    <p>Putting products into consumers' hands through targeted sampling that drives trial, builds product understanding, and converts interest into purchase.</p>
  </article>
</section>

<!-- What we do -->
<section class="slide services" style="left:58px;top:604px">
  <div class="brand"><span class="brand-mark"></span><span class="brand-name">BRIGHT<br>SATCHEL</span></div>
  <h2 class="slide-title" style="top:10px">What We Do</h2>
  <article class="service" style="left:10px;top:51px;width:100px">
    <span class="icon"></span><h3>Pop-Up Stores &amp;<br>Brand Installations</h3>
    <p>We build temporary, immersive retail experiences that bring brands to life.</p>
  </article>
  <article class="service" style="left:115px;top:51px;width:100px">
    <span class="icon"></span><h3>Roadshows</h3>
    <p>We run branded mobile tours with multi-city stops across festivals, retail, and events, featuring live demos, competitions, and giveaways.</p>
  </article>
  <article class="service" style="left:221px;top:51px;width:100px">
    <span class="icon"></span><h3>Guerrilla Sampling</h3>
    <p>We deploy in high-street, supermarket, and hotspot locations to reach targeted audiences quickly and effectively.</p>
  </article>
  <article class="service" style="left:326px;top:51px;width:100px">
    <span class="icon"></span><h3>Events &amp; Trade Shows</h3>
    <p>We provide fully staffed activations with interactive experiences, games, challenges, and data capture.</p>
  </article>
  <article class="service" style="left:10px;top:145px;width:134px">
    <span class="icon"></span><h3>Product Sampling Activations</h3>
    <p>We deliver high-footfall sampling, branded pop-ups and stands, and engagement-led staff focused on capturing data and feedback.</p>
  </article>
  <article class="service" style="left:150px;top:145px;width:134px">
    <span class="icon"></span><h3>In-Store Demonstrations</h3>
    <p>Across supermarkets, electronics, beauty, and more, our teams showcase product benefits to drive instant sales.</p>
  </article>
  <article class="service" style="left:292px;top:145px;width:134px">
    <span class="icon"></span><h3>Cash &amp; Carry — Depot Days</h3>
    <p>We drive active selling and sampling, engage trade customers, and support with POS and creative engagement ideas.</p>
  </article>
</section>

<!-- We do it all -->
<section class="slide all" style="left:528px;top:607px">
  <div class="brand"><span class="brand-mark"></span><span class="brand-name">BRIGHT<br>SATCHEL</span></div>
  <h2 class="slide-title" style="top:10px">We Do It All</h2>
  <div class="abs all-photo" role="img" aria-label="Shopper trying a product sample with a brand ambassador"></div>
  <div class="all-block" style="top:20px">
    <h3>How We Work</h3>
    <p>We deliver high-quality brand activations through our nationwide team of trained specialists, including Brand Ambassadors, Event Managers, Sampling Teams, Product Demonstrators, and pop-up Activation Crews. Our people are at the heart of every activation - professional, engaging, and trained to represent your brand flawlessly.</p>
  </div>
  <div class="abs all-rule" style="top:87px"></div>
  <div class="all-block" style="top:109px">
    <h3>Where We Activate</h3>
    <p>We deploy across multiple environments to meet audiences where they already are, including retail, wholesale cash &amp; carry, events and festivals, and guerrilla or high - footfall locations.</p>
  </div>
  <div class="abs all-rule" style="top:159px"></div>
  <div class="all-block" style="top:181px">
    <h3>How We Can Help</h3>
    <p>From everyday sampling to large-scale experiences, we support brands across sampling and trial, supermarket sampling, convenience retail sampling, consumer event sampling, sampling to trade, and trade shows.</p>
  </div>
</section>

<!-- Invest -->
<section class="slide invest" style="left:58px;top:877px">
  <div class="brand"><span class="brand-mark"></span><span class="brand-name">BRIGHT<br>SATCHEL</span></div>
  <h2 class="slide-title" style="top:12px">Invest</h2>
  <svg class="chart" width="433" height="243" viewBox="0 0 433 243" role="img" aria-label="Line chart of two monthly series from January to December">
    <g stroke="var(--grid)" stroke-width=".5">
      <line x1="23" y1="64" x2="420" y2="64"/><line x1="23" y1="77.6" x2="420" y2="77.6"/><line x1="23" y1="91.2" x2="420" y2="91.2"/><line x1="23" y1="104.8" x2="420" y2="104.8"/><line x1="23" y1="118.4" x2="420" y2="118.4"/><line x1="23" y1="132" x2="420" y2="132"/><line x1="23" y1="145.6" x2="420" y2="145.6"/><line x1="23" y1="159.2" x2="420" y2="159.2"/><line x1="23" y1="172.8" x2="420" y2="172.8"/><line x1="23" y1="186.4" x2="420" y2="186.4"/><line x1="23" y1="200" x2="420" y2="200"/>
      <line x1="23" y1="64" x2="23" y2="200"/><line x1="56.1" y1="64" x2="56.1" y2="200"/><line x1="89.2" y1="64" x2="89.2" y2="200"/><line x1="122.3" y1="64" x2="122.3" y2="200"/><line x1="155.3" y1="64" x2="155.3" y2="200"/><line x1="188.4" y1="64" x2="188.4" y2="200"/><line x1="221.5" y1="64" x2="221.5" y2="200"/><line x1="254.6" y1="64" x2="254.6" y2="200"/><line x1="287.7" y1="64" x2="287.7" y2="200"/><line x1="320.8" y1="64" x2="320.8" y2="200"/><line x1="353.8" y1="64" x2="353.8" y2="200"/><line x1="386.9" y1="64" x2="386.9" y2="200"/><line x1="420" y1="64" x2="420" y2="200"/>
    </g>
    <g text-anchor="end">
      <text x="20" y="65.3">100</text><text x="20" y="78.9">90</text><text x="20" y="92.5">80</text><text x="20" y="106.1">70</text><text x="20" y="119.7">60</text><text x="20" y="133.3">50</text><text x="20" y="146.9">40</text><text x="20" y="160.5">30</text><text x="20" y="174.1">20</text><text x="20" y="187.7">10</text><text x="20" y="201.3">0</text>
    </g>
    <g text-anchor="middle">
      <text x="39.5" y="209">JAN</text><text x="72.6" y="209">FEB</text><text x="105.7" y="209">MAR</text><text x="138.8" y="209">APR</text><text x="171.9" y="209">MAY</text><text x="205" y="209">JUN</text><text x="238" y="209">JUL</text><text x="271.1" y="209">AUG</text><text x="304.2" y="209">SEP</text><text x="337.3" y="209">OCT</text><text x="370.4" y="209">NOV</text><text x="403.5" y="209">DEC</text>
    </g>
    <polyline fill="none" stroke="var(--chart-green)" stroke-width=".8" points="23,145.6 56.1,132 89.2,145.6 122.3,104.8 155.3,104.8 188.4,118.4 221.5,104.8 254.6,104.8 287.7,83 320.8,77.6 353.8,77.6 386.9,83 420,77.6"/>
    <g fill="var(--chart-green)">
      <circle cx="23" cy="145.6" r="1.5"/><circle cx="56.1" cy="132" r="1.5"/><circle cx="89.2" cy="145.6" r="1.5"/><circle cx="122.3" cy="104.8" r="1.5"/><circle cx="155.3" cy="104.8" r="1.5"/><circle cx="188.4" cy="118.4" r="1.5"/><circle cx="221.5" cy="104.8" r="1.5"/><circle cx="254.6" cy="104.8" r="1.5"/><circle cx="287.7" cy="83" r="1.5"/><circle cx="320.8" cy="77.6" r="1.5"/><circle cx="353.8" cy="77.6" r="1.5"/><circle cx="386.9" cy="83" r="1.5"/><circle cx="420" cy="77.6" r="1.5"/>
    </g>
    <polyline fill="none" stroke="var(--chart-pink)" stroke-width=".8" points="23,186.4 56.1,159.2 89.2,172.8 122.3,132 155.3,118.4 188.4,145.6 221.5,132 254.6,145.6 320.8,91.2 386.9,118.4 420,91.2"/>
    <g fill="var(--chart-pink)">
      <circle cx="23" cy="186.4" r="1.5"/><circle cx="56.1" cy="159.2" r="1.5"/><circle cx="89.2" cy="172.8" r="1.5"/><circle cx="122.3" cy="132" r="1.5"/><circle cx="155.3" cy="118.4" r="1.5"/><circle cx="188.4" cy="145.6" r="1.5"/><circle cx="221.5" cy="132" r="1.5"/><circle cx="254.6" cy="145.6" r="1.5"/><circle cx="320.8" cy="91.2" r="1.5"/><circle cx="386.9" cy="118.4" r="1.5"/><circle cx="420" cy="91.2" r="1.5"/>
    </g>
  </svg>
</section>

<!-- Thank you -->
<section class="slide thanks" style="left:528px;top:880px">
  <div class="abs brand-block"><span class="brand-mark"></span><span class="brand-name">BRIGHT<br>SATCHEL</span></div>
  <div class="abs thanks-rule" style="top:66px"></div>
  <h2 class="abs thanks-title">Thank You</h2>
  <div class="abs thanks-rule pink" style="top:174px"></div>
</section>

</body>
</html>
```